Intermodal Trucking Company Website

My client is a trucking company that takes the containers you see on the back of a ship or railroad car and delivers them in the midwestern part of the United States. Here are some of their competitors Websites and their logo to use as part of the design.

http://www.varnekhaulers.example/
https://www.plirext.example/
http://www.brontagefreight.example/
https://www.lqp-xy.example/

Industry/Entity Type

Trucking Company

Number of Pages Required

2 page

Requirements
Must have
• Website must be professional and the design needs to be suitable for a responsive Website.
Should not have
• Please do not submit designs with misspellings. Designs with misspellings will be eliminated.

```html
<!DOCTYPE html>
<html lang="en">
<head>
<meta charset="utf-8">
<title>Tallgrass Haul Co. — Intermodal Trucking</title>
<link href="https://fonts.googleapis.com/css2?family=Raleway:wght@400;500;600;700&family=Open+Sans:wght@400;600;700&display=swap" rel="stylesheet">
<style>
:root{
  --red:#e5202e;
  --red-dark:#c9141f;
  --ink:#222;
  --body:#555;
  --muted:#777;
  --footer:#f4f4f4;
  --rule:#cfcfcf;
  --white:#fff;
}
*{margin:0;padding:0;box-sizing:border-box}
html,body{width:743px;height:1200px;overflow:hidden;background:var(--white)}
body{position:relative;font-family:"Open Sans",sans-serif;color:var(--body)}
.abs{position:absolute}
.header{left:0;top:0;width:743px;height:69px;background:var(--white)}
.brand{left:78px;top:20px;display:flex;align-items:center;gap:6px;font-family:"Open Sans",sans-serif;font-weight:700;font-size:12px;color:var(--red)}
.brand .dot{width:10px;height:10px;border-radius:50%;background:var(--red)}
.callbar{right:93px;top:13px;display:flex;align-items:center;gap:5px;font-size:6.5px;color:var(--ink)}
.callbar .lbl{color:var(--red)}
.social{display:flex;gap:4px;margin-left:8px}
.social span{width:17px;height:17px;border-radius:50%;background:var(--red);display:block}
.nav{top:46px;left:0;width:743px;font-size:8px;color:var(--ink);font-family:"Open Sans",sans-serif}
.nav a{position:absolute;text-decoration:none;color:inherit;white-space:nowrap}
.nav a.active{color:var(--red)}
.hero{left:0;top:69px;width:743px;height:272px;background:linear-gradient(160deg,#9fb7d6 0%,#d9dee4 35%,#c7c9cc 60%,#8d8f92 100%)}
.hero-box{left:82px;top:153px;width:255px;height:135px;background:rgba(60,60,60,.72);padding:16px 18px}
.hero-box h1{font-family:"Raleway",sans-serif;font-weight:600;font-size:20.5px;color:var(--white);margin-top:2px}
.hero-box p{font-size:6.5px;line-height:12px;color:#eee;margin-top:10px}
.btn{display:inline-block;background:var(--red);color:var(--white);font-size:6.5px;font-weight:600;border-radius:2px;text-align:center}
.hero-box .btn{margin-top:12px;width:79px;height:22px;line-height:22px}
.arrow{top:195px;width:30px;height:29px;background:rgba(90,90,90,.55)}
.arrow svg{display:block;margin:9px auto}
.welcome h2,.sec-title{font-family:"Raleway",sans-serif;font-weight:400;text-align:center;width:743px;left:0}
.welcome h2{position:absolute;top:368px;font-size:22px;color:var(--red)}
.welcome p{position:absolute;left:80px;top:410px;width:580px;text-align:center;font-size:6.5px;line-height:12px;color:var(--body)}
.welcome .btn{position:absolute;left:343px;top:466px;width:56px;height:20px;line-height:20px}
.services{left:0;top:529px;width:743px;height:260px;background:var(--red)}
.services .sec-title{position:absolute;top:30px;font-size:21px;color:var(--white)}
.card{top:93px;width:186px;height:127px}
.card span{position:absolute;left:0;bottom:10px;width:100%;text-align:center;font-family:"Raleway",sans-serif;font-weight:700;font-size:10.5px;color:var(--white)}
.news .sec-title{position:absolute;top:810px;font-size:21px;color:var(--red)}
.news-img{top:874px;width:106px;height:89px}
.news-text{top:870px;width:150px}
.news-text h3{font-family:"Raleway",sans-serif;font-weight:500;font-size:12px;color:var(--red)}
.news-text p{font-size:6.5px;line-height:12px;margin-top:9px}
.news-text .btn{margin-top:9px;width:56px;height:20px;line-height:20px}
.footer{left:0;top:1009px;width:743px;height:191px;background:var(--footer)}
.footer .brand{left:82px;top:40px}
.fcol{top:29px}
.fcol h4{font-family:"Open Sans",sans-serif;font-weight:400;font-size:8.5px;color:var(--red)}
.fcol ul{list-style:none;margin-top:6px}
.fcol li{font-size:6.3px;line-height:15px;color:var(--muted)}
.fcol p{font-size:6.3px;line-height:15px;color:var(--muted);margin-top:6px}
.field{width:155px;height:25px;border:1px solid #d8d8d8;background:var(--white);font-size:6.3px;line-height:23px;padding-left:9px;color:#666;margin-top:11px}
.fcol .btn{margin-top:12px;width:51px;height:17px;line-height:17px;font-weight:400;font-size:6.2px}
.contact li{display:flex;gap:7px;align-items:flex-start;line-height:9px;margin-bottom:8px}
.contact svg{flex:none;margin-top:1px}
.rule{left:82px;top:1163px;width:581px;height:1px;background:var(--rule)}
.copy{left:0;top:1175px;width:743px;text-align:center;font-size:6.3px;color:var(--ink)}
</style>
</head>
<body>

<header class="abs header">
  <div class="abs brand"><span class="dot"></span>Tallgrass Haul Co.</div>
  <div class="abs callbar">
    <svg width="7" height="7" viewBox="0 0 24 24"><path fill="#e5202e" d="M6.6 10.8a15 15 0 0 0 6.6 6.6l2.2-2.2c.3-.3.7-.4 1-.2 1.1.4 2.3.6 3.6.6.6 0 1 .4 1 1V20c0 .6-.4 1-1 1A17 17 0 0 1 3 4c0-.6.4-1 1-1h3.5c.6 0 1 .4 1 1 0 1.3.2 2.5.6 3.6.1.3 0 .7-.2 1z"/></svg>
    <span class="lbl">CALL US :</span><span>1800 555 0142</span>
    <div class="social"><span></span><span></span></div>
  </div>
  <nav class="abs nav">
    <a class="active" style="left:363px">HOME</a>
    <a style="left:417px">ABOUT US</a>
    <a style="left:490px">SERVICES</a>
    <a style="left:558px">NEWS</a>
    <a style="left:612px">CONTACT US</a>
  </nav>
</header>

<section class="abs hero" role="img" aria-label="White semi truck with a long trailer parked at a loading dock"></section>
<div class="abs arrow" style="left:36px"><svg width="8" height="12" viewBox="0 0 8 12"><path d="M7 1 2 6l5 5" stroke="#fff" fill="none"/></svg></div>
<div class="abs arrow" style="left:676px"><svg width="8" height="12" viewBox="0 0 8 12"><path d="M1 1l5 5-5 5" stroke="#fff" fill="none"/></svg></div>
<div class="abs hero-box">
  <h1>Intermodal Trucking</h1>
  <p>Lorem ipsum dolor sit amet, consectetur adipiscing elit, sed do eiusmod tempor incididunt</p>
  <span class="btn">Request Quote</span>
</div>

<section class="welcome">
  <h2>Welcome to Tallgrass Haul Co.</h2>
  <p>Call us for all you Intermodal container movement needs out of the Kansas City, KS or MO area. &nbsp;We have been in business for over 20 years handeling all types of container movement including hazmat movements to anywhere within the 48 states. Tallgrass has been in business for over 20 years in the Intermodal Container business. &nbsp;We currently store containers for Meridian Sea Lines, Vega Star shipping and Ketra off hire container.</p>
  <span class="btn">Read More</span>
</section>

<section class="abs services">
  <h2 class="sec-title">Our Services</h2>
  <div class="abs card" style="left:82px;background:linear-gradient(160deg,#b9c3cf,#2b3345 55%,#6d6d6d)" role="img" aria-label="Dark blue truck cab on a highway"><span>VEGA STAR SHIPPING</span></div>
  <div class="abs card" style="left:279px;background:linear-gradient(170deg,#c9d6e6,#6c7a86 45%,#2f4a8a 70%,#808488)" role="img" aria-label="Row of blue semi trucks parked in line"><span>FORKLIFTS</span></div>
  <div class="abs card" style="left:477px;background:linear-gradient(160deg,#2c3850,#6a7690 45%,#3a3226 80%,#7a5a2a)" role="img" aria-label="Truck under a stormy evening sky"><span>LARGE MACHINES</span></div>
</section>

<section class="news">
  <h2 class="sec-title">Recent News</h2>
  <div class="abs news-img" style="left:82px;background:linear-gradient(160deg,#8fb07a,#d8dde6 45%,#3b58a8 75%,#c04a6a)" role="img" aria-label="Colourful semi trucks parked side by side"></div>
  <div class="abs news-text" style="left:205px">
    <h3>Lorem ipsum dolor</h3>
    <p>Nemo enim ipsam voluptatem quia voluptas sit aspernatur aut odit aut fugit, sed quia consequuntur magni</p>
    <span class="btn">Read More</span>
  </div>
  <div class="abs news-img" style="left:394px;background:linear-gradient(160deg,#c6d4e2,#a0714a 40%,#3aa0b0 70%,#707070)" role="img" aria-label="Teal log truck loaded with timber"></div>
  <div class="abs news-text" style="left:517px">
    <h3>Lorem ipsum dolor</h3>
    <p>Nemo enim ipsam voluptatem quia voluptas sit aspernatur aut odit aut fugit, sed quia consequuntur magni</p>
    <span class="btn">Read More</span>
  </div>
</section>

<footer class="abs footer">
  <div class="abs brand"><span class="dot"></span>Tallgrass Haul Co.</div>
  <div class="abs fcol" style="left:239px">
    <h4>QUICK LINKS</h4>
    <ul><li>Home</li><li>About us</li><li>Services</li><li>News</li><li>Contact us</li></ul>
  </div>
  <div class="abs fcol" style="left:359px">
    <h4>NEWSLETTER</h4>
    <p>Enter your email address to receive the latest<br>news and notes from our blog.</p>
    <div class="field">Enter Your Mail Id</div>
    <span class="btn">SUBSCRIBE</span>
  </div>
  <div class="abs fcol contact" style="left:560px">
    <h4>CONTACT US</h4>
    <ul style="margin-top:9px">
      <li><svg width="7" height="7" viewBox="0 0 10 10"><path d="M1 3c2-2 6-2 8 0v1H7V3H3v1H1zM2 5h6l1 4H1z" fill="#666"/></svg>(555) 210-3347</li>
      <li><svg width="7" height="7" viewBox="0 0 10 10"><path d="M2 1h6v3H2zM1 4h8v4H7v2H3V8H1z" fill="#666"/></svg>(555) 210-3347</li>
      <li><svg width="7" height="7" viewBox="0 0 10 10"><path d="M0 2h10v6H0zM0 2l5 4 5-4" fill="#666" stroke="#f4f4f4" stroke-width=".6"/></svg><span style="text-decoration:underline">info@tallgrasshaul.example</span></li>
      <li><svg width="7" height="8" viewBox="0 0 10 12"><path d="M5 0a4 4 0 0 1 4 4c0 3-4 8-4 8S1 7 1 4a4 4 0 0 1 4-4z" fill="#666"/><circle cx="5" cy="4" r="1.5" fill="#f4f4f4"/></svg>#2868 Lorem ipsum dolor sit<br>amet, consectetur</li>
    </ul>
  </div>
</footer>
<div class="abs rule"></div>
<div class="abs copy">©2017 tallgrasshaul.example. All Rights Reserved.</div>

</body>
</html>
```